QUILLARRA CAPABILITY STATEMENT “Building Tomorrow Today”

QUILLARRA CAPABILITY STATEMENT
“Building Tomorrow Today”
Indigenous-Owned Telecommunications & Infrastructure Solutions Partner

COVER PAGE

Visual: Modern and clean design featuring telecom towers, wind turbines, civil infrastructure, roads, and community WiFi imagery.
Tagline: “Connecting Communities, Powering Progress.”
Contact:
Website: www.quillarra.example.au
Email: info@quillarra.example.au
Phone: [Insert Main Number]
“Proudly Indigenous-Owned | Compliant with Native Sourcing Charter (NSC) & SME Policies”
INTRODUCTION

Quillarra is a 100% Indigenous-owned leader in comprehensive infrastructure solutions, specializing in telecommunications, civil works, renewable energy, structural engineering, and site development. With over a decade of experience, we deliver safe, reliable, and culturally respectful services across Australia, from urban centers to remote wind farms and heritage sites. Our mission: “To bridge infrastructure gaps while empowering Indigenous communities and fostering sustainable growth.”

CORE CAPABILITIES

TELECOMMUNICATIONS

Tower Builds & Maintenance: Structural engineering, geotechnical analysis, foundation mapping.
Community WiFi Projects: Enhancing digital inclusion in Indigenous and remote communities.
Fiber & Wireless Networks: End-to-end installation for KPX, Satellite, and regional connectivity.
Height Safety Systems: Design, inspection, and certification of lad-safe safety infrastructure.
CIVIL & STRUCTURAL ENGINEERING

Foundations & Concreting: Reinforced slabs, grillage, geotech-to-construction turnkey solutions.
Site Development: Earthworks, drainage, and access road/track construction.
Wind Farm Infrastructure: Reinforcing towers and integrating power systems for high-wind environments.
ROAD & ACCESS TRACK CONSTRUCTION

Construction of durable access roads and tracks: For remote projects and urban settings.
Remediation of existing tracks: Upgrading for environmental compliance and sustainability.
Facilitating logistics and site access: Particularly in challenging terrain.
POWER & ELECTRICAL SYSTEMS

Off-grid energy solutions: Solar hybrid systems, electrical structural engineering.
Grid upgrades: Ensuring compliance with AS/NZS standards and facilitating connection upgrades.
SITE REFURBISHMENT & DEMOLITION

Comprehensive refurbishment and demolition services: For outdated telecom sites and structures.
Environmentally responsible dismantling: Focused on recycling materials and minimizing land impact.
EMERGENCY RESPONSE SERVICES

24/7 Rapid Response: Over 450 callouts annually; 4,000+ emergencies resolved nationwide.
Disaster Recovery: Comprehensive support during floods, bushfires for KPX, Dunholt, Marigane, and regional clients.
PROJECT EXPERIENCE

Heritage Tower Upgrade

Enhanced safety and technology on culturally significant heritage sites, preserving their integrity.
Wind Farm Deployment

Delivered power, fiber, and reinforced foundations for large-scale renewable energy projects in high-wind environments.
Regional Fibre Network

Laid 200km of fiber in flood-prone regions, ensuring critical infrastructure resilience.
Indigenous Community WiFi & Connectivity

Installed sustainable WiFi networks to bridge the digital divide, supporting education, health, and business activities.
Site Demolition & Refurbishment

Safely decommissioned aging telecom sites and structures across Australia, emphasizing land reuse and environmental care.
Access Track Construction & Remediation

Developed new access roads and refurbished existing tracks to facilitate project logistics, particularly in remote or environmentally sensitive areas.
Key Stats:
+600 sites supported | 10-year KPX partner | 98% client retention | Over 20 Indigenous community WiFi deployments

COMMITMENT TO SAFETY & QUALITY

“Pause Before You Climb” Protocol: Enforced pre-task risk assessments to ensure safety at every stage.
Certifications: ISO 45001 (Safety) | ISO 9001 (Quality Management).
Safety Culture: Regular safety audits, Indigenous-led training programs, and safety initiatives focused on community well-being.
INDIGENOUS INCLUSION & COMMUNITY IMPACT

Aboriginal Advisory Board: Provides guidance on community engagement, cultural sensitivity, and social responsibility.
Supplier Diversity: 30% procurement from Indigenous-owned businesses, fostering economic growth.
Regional Employment: 65% of our workforce originates from local communities, creating sustainable jobs.
Testimonial: “Quillarra’s partnership empowered our community with jobs and infrastructure that respects our land.” – Local Indigenous Leader

CONTACT & SERVICE AREAS

Headquarters: [Insert Address] | ABN: [Insert ABN]

24/7 Emergency Support: [Insert Dedicated Emergency Line]

Certifications & Registrations:

Vendor Circle Registered, First Trade Registry (FTR)
SERVICE AREAS

National Coverage with Regional Expertise:
Major Cities: Sydney, Melbourne, Brisbane, Perth, Adelaide, Darwin, Hobart.
Regional & Remote Areas: Pilbara, Kimberley, Far North Queensland, Outback NSW.
Disaster Zones: Rapid response teams deployed nationwide for bushfire and flood incidents.
EMERGENCY SUPPORT

SLA Guarantee: 90% of emergencies addressed within 4 hours.
Partners Supported: KPX, Dunholt, Marigane, regional councils.
This capability statement reflects our commitment to quality, safety, and community engagement across all levels of operation, ensuring that we empower the communities we serve while maintaining the highest standards of service delivery.

Target Market(s)

Government Agencies: Especially those seeking to comply with Indigenous Procurement Policies. Telecommunication Operators: Such as KPX, Dunholt, and Marigane for infrastructure deployment. Indigenous Communities: Projects aimed at enhancing connectivity and digital inclusion. Utilities and Energy Providers: For power and electrical infrastructure projects. Construction and Engineering Firms: Seeking collaboration on civil and structural infrastructure projects.

Industry/Entity Type

Telecommunications and Infrastructure Development: Focused on service delivery in various contexts, including urban settings, remote locations, and Indigenous community projects. Renewable Energy: This includes wind and solar infrastructure linked to telecommunications enhancements. Civil Engineering: Related to building and maintaining essential infrastructure such as access roads and utility lines.

Font styles to use
Other font styles liked:
• Bubbleboddy neue

Requirements
Must have
• Clear demonstration of Indigenous ownership and community engagement. Compliance with relevant safety and quality certifications (e.g., ISO 45001, ISO 9001). Showcase of core capabilities in telecommunications, civil engineering, and those specific to renewable energy. Visuals that reflect the diverse range of services offered (like telecom towers and community WiFi installations).
Nice to have
• Interactive elements such as hyperlinks to project case studies or client testimonials. Infographics or visual data to highlight key statistics and project success rates. Cultural motifs or imagery that reflect Indigenous heritage and inclusion in design aspirations. QR codes that link to videos or more detailed project descriptions for digital formats.
Should not have
• Clutter or excessive text that detracts from the main messages. Generic stock images that don’t align with the specific projects or Indigenous culture. Technical jargon that could confuse stakeholders unfamiliar with industry-specific terms. Overemphasis on competitors; the focus should remain on Quillarra's unique strengths and contributions.

```html
<!DOCTYPE html>
<html lang="en">
<head>
<meta charset="utf-8">
<title>Quillarra – Indigenous Inclusion</title>
<link href="https://fonts.googleapis.com/css2?family=Barlow:wght@400;600&family=Righteous&display=swap" rel="stylesheet">
<style>
  :root {
    --brand-red: #e8232a;
    --ink: #1a1a1a;
    --paper: #ffffff;
  }
  html, body { margin: 0; padding: 0; overflow: hidden; background: var(--paper); }
  .page {
    position: relative;
    width: 927px;
    height: 1200px;
    overflow: hidden;
    background: var(--paper);
    font-family: "Barlow", sans-serif;
    color: var(--ink);
  }
  .corner { position: absolute; }
  .corner--top { top: 0; right: 0; }
  .corner--bottom { bottom: 0; left: 0; }
  .section-title {
    position: absolute;
    left: 78px;
    margin: 0;
    font-family: "Righteous", sans-serif;
    font-weight: 400;
    color: var(--brand-red);
    font-size: 22.5px;
    line-height: 26px;
    letter-spacing: -0.6px;
    text-transform: uppercase;
  }
  .item {
    position: absolute;
    left: 78px;
    margin: 0;
    font-size: 20.5px;
    line-height: 25.5px;
  }
  .item-title { font-weight: 600; font-size: 21.5px; display: block; line-height: 26px; }
  .item-title--inline { display: inline; }
  .partner {
    position: absolute;
    top: 1126px;
    height: 30px;
    display: flex;
    align-items: center;
    gap: 8px;
    font-family: "Barlow", sans-serif;
    font-weight: 600;
    font-size: 17px;
    color: var(--ink);
    white-space: nowrap;
  }
  .partner-mark {
    width: 12px;
    height: 12px;
    background: var(--brand-red);
    flex: none;
  }
</style>
</head>
<body>
<main class="page">
  <svg class="corner corner--top" width="267" height="104" viewBox="0 0 267 104" role="img" aria-label="Red chevron band with Aboriginal dot-circle pattern">
    <polygon points="0,0 133,103 267,0 198,0 133,48 67,0" fill="var(--brand-red)"/>
  </svg>
  <svg class="corner corner--bottom" width="264" height="104" viewBox="0 0 264 104" role="img" aria-label="Red chevron band with Aboriginal dot-circle pattern">
    <polygon points="0,104 0,85 131,0 264,104 198,104 131,55 62,104" fill="var(--brand-red)"/>
  </svg>

  <h1 class="section-title" style="top:108px;">Indigenous Inclusion</h1>

  <p class="item" style="top:163px;"><span class="item-title">Native Sourcing Charter Compliance:</span>As an Indigenous-owned business, we inherently support the objectives<br>of the Native Sourcing Charter. Promoting economic opportunities<br>for Indigenous businesses and communities.</p>

  <p class="item" style="top:294px;"><span class="item-title">Engagement with Indigenous Communities:</span>Actively engaging with Indigenous communities, respecting their cultural heritage,<br>and providing opportunities for collaboration and employment.</p>

  <p class="item" style="top:399px;"><span class="item-title">Supplier Diversity:</span>Prioritising sourcing goods and services from Indigenous suppliers whenever possible.<br>Contributing to the growth and sustainability of Indigenous businesses.</p>

  <p class="item" style="top:504px;"><span class="item-title">SME and Regional Procurement Policy Compliance:</span>Recognising the importance of supporting SMEs and regional businesses<br>in the procurement process. Actively seeking partnerships with local suppliers<br>and subcontractors, fostering economic growth and job creation<br>in the regions where we operate.</p>

  <p class="item" style="top:660px;"><span class="item-title">Regional Engagement:</span>Prioritising local hiring and procurement, investing in the communities where we work.</p>

  <h2 class="section-title" style="top:737px;">Ensuring that our projects contribute to<br>regional development and prosperity.</h2>

  <p class="item" style="top:817px;"><span class="item-title">Aboriginal and Torres Strait Islander Advisory Board:</span>Constructing true respectful communication in community.</p>

  <p class="item" style="top:897px;"><span class="item-title item-title--inline">Form Connections:</span> Establish and nurture meaningful relationships<br>with local Indigenous communities.</p>

  <div class="partner" style="left:318px;"><span class="partner-mark"></span>Yarrun</div>
  <div class="partner" style="left:505px;"><span class="partner-mark"></span>Mirrabel</div>
  <div class="partner" style="left:660px;"><span class="partner-mark"></span>Tallowin</div>
  <div class="partner" style="left:765px;"><span class="partner-mark"></span>Koorin Group</div>
</main>
</body>
</html>
```